Website Revamp to a Legal Tech Company

We are a Legal Technology Company and we are revamping our whole company from the logo (already done) to the website. We have built a custom portal and harnessed the use of AI and automation.

Current Website - https://www.velmarix.com/

We need a new website that looks like a tech company
Some examples of websites for samples
1. What we have today - https://www.velmarix.com/
2. https://pinwolegal.com/
3. https://www.brimfoxhub.com/
4. https://www.taru.com/
5.https://www.sotrimlaw.com/
6. https://www.murabex.com/

Hope this helps. Let's start with the Home page.
Once we agree on the basis design and the first 3-4 pages - we can handle the coding etc. Will have the content over once we have the basic homepage design.

Links that we will possibly have and want
1. Home
2. About Us
3. Place your Order
4. Free First File offer to all new customers
5. Services/Products
6. Transparent Pricing
7. Contact Us

Terms & Conditions and Privacy Policy will be added at the bottom of the page but our internal designers.

Hope this helps.

Target Market(s)

Personal Injury Law Firms in the US

Industry/Entity Type

Legal Tech Services

Coding

Coded - Design and coding required

Number of Pages Required

4 page

Colors

Designer to choose colors to be used in the design.

Requirements
Must have
• Need to look like a Tech company website
Nice to have
• The color Blue

```html
<!DOCTYPE html>
<html lang="en">
<head>
<meta charset="utf-8">
<title>Velmarix — Retrieval of Medical Records</title>
<link href="https://fonts.googleapis.com/css2?family=Poppins:wght@400;500;600;700;800&family=Roboto:wght@400;500;700&display=swap" rel="stylesheet">
<style>
:root{
  --navy:#0b2a55;
  --navy-deep:#061c3d;
  --blue:#124a8c;
  --blue-mid:#1c5ea8;
  --ice:#eef3fa;
  --ink:#111418;
  --muted:#6b7380;
  --line:#dde4ee;
  --white:#ffffff;
  --black:#050608;
}
*{margin:0;padding:0;box-sizing:border-box}
html,body{width:1200px;height:4684px;overflow:hidden}
body{position:relative;font-family:"Roboto",Arial,sans-serif;color:var(--ink);background:var(--white)}
.abs{position:absolute}
h1,h2,h3,.title{font-family:"Poppins",Arial,sans-serif}
.btn{position:absolute;display:flex;align-items:center;justify-content:center;gap:8px;background:var(--navy);color:var(--white);font:700 12px "Roboto",sans-serif;letter-spacing:.3px;border-radius:22px;text-transform:uppercase}
.btn .dot{width:11px;height:11px;border-radius:50%;background:var(--white);display:inline-flex;align-items:center;justify-content:center}
.btn .dot::after{content:"";border-left:4px solid var(--navy);border-top:3px solid transparent;border-bottom:3px solid transparent;margin-left:1px}
.bars{display:inline-flex;flex-direction:column;gap:4px;vertical-align:middle}
.bars i{display:block;height:4px;background:var(--navy);border-radius:1px}
.section-title{position:absolute;left:0;width:1200px;display:flex;justify-content:center;align-items:center;gap:22px;font:800 34px "Poppins",sans-serif;color:var(--ink)}
.section-title .bars i:nth-child(1){width:52px}.section-title .bars i:nth-child(2){width:40px;margin-left:12px}.section-title .bars i:nth-child(3){width:52px}

/* hero */
.hero{left:0;top:0;width:1200px;height:690px;overflow:hidden}
.hero-photo{left:0;top:0;width:1200px;height:690px;background:linear-gradient(90deg,#3a2417 0%,#6a3f26 28%,#a7acb4 55%,#d8dde3 75%,#a9b6c2 100%)}
.hero-shade{left:0;top:0;width:1200px;height:690px;background:linear-gradient(90deg,rgba(20,12,8,.55) 0%,rgba(20,12,8,.25) 45%,rgba(0,0,0,0) 70%)}
.logo{display:flex;align-items:center;gap:8px;color:var(--white);font:700 22px "Poppins",sans-serif}
.logo .mark{width:14px;height:14px;border-radius:50%;background:currentColor}
.top-contact{top:22px;display:flex;align-items:center;gap:12px;color:var(--white);font:500 14px "Roboto",sans-serif}
.top-contact .ico{width:28px;height:28px;background:var(--white);border-radius:4px;display:flex;align-items:center;justify-content:center}
.nav{left:258px;top:90px;display:flex;gap:41px;color:var(--white);font:700 13px "Roboto",sans-serif}
.hero h1{left:145px;top:222px;color:var(--white);font-weight:500;font-size:40px;line-height:62px;letter-spacing:.5px}
.hero h1 strong{font-weight:800;font-size:41px}
.hero p{left:147px;top:356px;width:440px;color:var(--white);font:700 14.5px/30px "Roboto",sans-serif}
.scroll-cue{left:1096px;top:254px;display:flex;flex-direction:column;gap:5px}
.scroll-cue i{width:0;height:0;border-left:6px solid transparent;border-right:6px solid transparent;border-top:9px solid var(--blue-mid)}

/* about */
.about-deco span{position:absolute;left:0;height:14px;background:var(--ice)}
.about-frame{left:193px;top:762px;width:362px;height:376px;border:2px solid var(--blue)}
.about-photo{left:207px;top:779px;width:336px;height:348px;border-radius:14px;background:linear-gradient(160deg,#8a5a33 0%,#b98b5a 35%,#e9e6e1 60%,#c54a2a 100%)}
.about-title{left:632px;top:764px;font:800 34px "Poppins",sans-serif;display:flex;align-items:center;gap:16px}
.about-title .bars i:nth-child(1){width:54px}.about-title .bars i:nth-child(2){width:40px}.about-title .bars i:nth-child(3){width:54px}
.about-text{left:632px;top:830px;width:352px;color:var(--muted);font:400 12.5px/24px "Roboto",sans-serif;text-align:justify}
.about-text p+p{margin-top:8px}

/* services */
.services{left:0;top:1238px;width:1200px;height:758px;background:var(--ice)}
.svc-card{position:absolute;top:1415px;width:396px;height:480px;background:var(--white);box-shadow:0 4px 18px rgba(11,42,85,.12);border:1px solid #e6ebf2}
.svc-photo{position:absolute;left:12px;top:12px;width:372px;height:258px;border-radius:18px}
.svc-icon{position:absolute;left:244px;top:215px;width:96px;height:96px;border-radius:50%;background:var(--navy);border:5px solid var(--white);display:flex;align-items:center;justify-content:center}
.svc-card h3{position:absolute;left:20px;top:322px;width:356px;text-align:center;font:600 16.5px/29px "Roboto",sans-serif;text-transform:uppercase}
.svc-card p{position:absolute;left:30px;top:392px;width:336px;text-align:center;color:var(--muted);font:400 13px/24px "Roboto",sans-serif}

/* offer */
.offer{left:144px;top:2093px;width:912px;height:350px;border-radius:26px;background:linear-gradient(120deg,#061f45 0%,#0b3a73 55%,#0f4a8c 100%);overflow:hidden;color:var(--white);text-align:center}
.offer h2{position:absolute;left:0;top:76px;width:912px;font:800 33px "Poppins",sans-serif}
.offer p{position:absolute;left:120px;top:154px;width:672px;font:400 13.5px/24px "Roboto",sans-serif}
.offer .btn{left:346px;top:236px;width:220px;height:40px;background:transparent;border:1.5px solid var(--white)}
.offer .btn .dot::after{border-left-color:var(--navy)}

/* why */
.why-title{left:146px;top:2564px;font:800 34px "Poppins",sans-serif;display:flex;align-items:center;gap:18px}
.why-title .bars i:nth-child(1){width:54px}.why-title .bars i:nth-child(2){width:40px}.why-title .bars i:nth-child(3){width:54px}
.why-line{left:186px;top:2700px;height:240px;border-left:2px dotted var(--blue)}
.why-item{position:absolute;left:146px;width:460px}
.why-item .ico{position:absolute;left:0;top:0;width:84px;height:84px;border-radius:50%;background:var(--navy);border:4px solid #dbe4f0;box-shadow:0 0 0 2px var(--white) inset;display:flex;align-items:center;justify-content:center}
.why-item h3{position:absolute;left:110px;top:-2px;font:700 15px "Roboto",sans-serif;letter-spacing:1px;text-transform:uppercase;white-space:nowrap}
.why-item p{position:absolute;left:110px;top:24px;width:340px;color:var(--muted);font:400 12.5px/24px "Roboto",sans-serif}
.why-photo{left:660px;top:2550px;width:410px;height:528px;border-radius:190px 190px 0 0;background:linear-gradient(180deg,#f4f1ec 0%,#c9864f 45%,#9a5e31 100%)}

/* cases */
.cases-bg{left:0;top:3070px;width:1200px;height:640px}
.hex{position:absolute;top:3345px;width:252px;height:262px}
.hex svg.shape{position:absolute;left:0;top:0}
.hex .tab{position:absolute;left:98px;top:0;width:56px;height:54px;background:var(--blue);border-radius:0 0 6px 6px;display:flex;align-items:center;justify-content:center}
.hex h3{position:absolute;left:0;top:84px;width:252px;text-align:center;font:500 14.5px "Roboto",sans-serif;text-transform:uppercase}
.hex p{position:absolute;left:34px;top:114px;width:184px;text-align:center;color:var(--muted);font:400 12.5px/24px "Roboto",sans-serif}
.hex .go{position:absolute;left:98px;top:206px;width:56px;height:56px;border-radius:50%;background:var(--white);border:1px solid #c8d2df;display:flex;align-items:center;justify-content:center}
.hex.active h3,.hex.active p{color:var(--white)}

/* message */
.msg-sub{left:0;top:3876px;width:1200px;text-align:center;color:var(--muted);font:400 13px "Roboto",sans-serif}
.field{position:absolute;height:52px;border-radius:26px;background:var(--white);box-shadow:0 3px 10px rgba(11,42,85,.12);border:1px solid #edf0f5;padding-left:26px;display:flex;align-items:center;font:400 10.5px "Roboto",sans-serif;color:#444;text-transform:uppercase}

/* footer */
.footer{left:0;top:4240px;width:1200px;height:444px}
.foot-col{position:absolute;top:4402px;color:var(--white);font:400 12.5px/24px "Roboto",sans-serif}
.foot-col h4{font:700 12.5px "Roboto",sans-serif;text-transform:uppercase;margin-bottom:12px}
.foot-row{display:flex;gap:14px;align-items:flex-start;margin-bottom:4px}
.foot-row svg{flex:none;margin-top:6px}
.quick a{display:block;color:var(--white);text-decoration:none}
.social{left:152px;top:4544px;display:flex;gap:18px}
.social span{width:13px;height:13px;border-radius:50%;background:var(--white)}
.foot-rule{left:344px;top:4610px;width:700px;border-top:1px solid #2a2f38}
.copyright{left:0;top:4636px;width:1200px;text-align:center;color:var(--white);font:400 12.5px "Roboto",sans-serif}
</style>
</head>
<body>

<!-- HERO -->
<section class="abs hero">
  <div class="abs hero-photo" role="img" aria-label="Photo of a doctor with a stethoscope reviewing medical paperwork in a hospital office"></div>
  <div class="abs hero-shade"></div>
  <div class="abs logo" style="left:145px;top:42px"><span class="mark"></span>Velmarix</div>
  <div class="abs top-contact" style="left:710px">
    <span class="ico"><svg width="14" height="11" viewBox="0 0 14 11"><rect x="0.5" y="0.5" width="13" height="10" rx="1" fill="none" stroke="#0b2a55"/><path d="M1 1l6 5 6-5" fill="none" stroke="#0b2a55"/></svg></span>info@velmarix.com
  </div>
  <div class="abs top-contact" style="left:912px">
    <span class="ico"><svg width="13" height="13" viewBox="0 0 24 24"><path d="M6.6 10.8a15 15 0 006.6 6.6l2.2-2.2a1 1 0 011-.25 11.4 11.4 0 003.6.6 1 1 0 011 1V20a1 1 0 01-1 1A17 17 0 013 4a1 1 0 011-1h3.5a1 1 0 011 1 11.4 11.4 0 00.6 3.6 1 1 0 01-.25 1z" fill="#0b2a55"/></svg></span>(555) 214-0870
  </div>
  <nav class="abs nav"><span>Home</span><span>About Us</span><span>Place your Order</span><span>Free First File Offer</span><span>Services</span><span>Transparent Pricing</span><span>Contact Us</span></nav>
  <h1 class="abs">RETRIEVAL OF<br><strong>MEDICAL RECORDS</strong></h1>
  <p class="abs">Get medical records and bills, as well as periodic follow-up with the medical provider to obtain updated records.</p>
  <div class="btn" style="left:147px;top:445px;width:166px;height:40px">Get Started <span class="dot"></span></div>
  <div class="abs scroll-cue"><i></i><i></i><i></i><i></i></div>
  <svg class="abs" style="left:0;top:540px" width="1200" height="150" viewBox="0 0 1200 150">
    <path d="M0 40 Q90 72 250 140 Q540 40 1200 55 L1200 150 L0 150 Z" fill="#0b2a55"/>
    <path d="M0 32 Q100 62 240 118 Q540 28 1200 40 L1200 150 L0 150 Z" fill="#ffffff"/>
    <path d="M0 62 Q120 90 240 108" fill="none" stroke="#0b2a55" stroke-width="3"/>
  </svg>
</section>

<!-- ABOUT -->
<section>
  <div class="about-deco"><span style="top:810px;width:168px"></span><span style="top:842px;width:168px"></span><span style="left:36px;top:876px;width:132px;background:#e4ebf5"></span></div>
  <div class="abs about-frame"></div>
  <div class="abs about-photo" role="img" aria-label="Photo of a smiling nurse holding folders in a medical records archive"></div>
  <h2 class="abs about-title">ABOUT US <span class="bars"><i></i><i></i><i></i></span></h2>
  <div class="abs about-text">
    <p>Velmarix employs a team with expertise in retrieving, assembling, reviewing, and summarizing medical records and bills. We support law firms by handling all medical records-related tasks, thereby allowing attorneys to focus on other very important case-related matters, such as proving liability, causation, and damages.</p>
    <p>Velmarix is equipped to immediately handle any size project for a small, mid-sized, or large law firm.</p>
  </div>
  <div class="btn" style="left:632px;top:1066px;width:146px;height:40px">View More <span class="dot"></span></div>
</section>

<!-- SERVICES -->
<section>
  <div class="abs services"></div>
  <h2 class="section-title" style="top:1322px"><span class="bars"><i></i><i></i><i></i></span>OUR SERVICES<span class="bars"><i></i><i></i><i></i></span></h2>
  <article class="svc-card" style="left:185px">
    <div class="svc-photo" role="img" aria-label="Photo of a desk with a computer and a hand reviewing printed medical forms" style="background:linear-gradient(135deg,#cfd6dd 0%,#eef1f4 45%,#9fb4cc 75%,#4f6f96 100%)"></div>
    <div class="svc-icon"><svg width="40" height="44" viewBox="0 0 40 44" fill="none" stroke="#fff" stroke-width="2"><rect x="6" y="4" width="28" height="36" rx="3"/><path d="M20 11v10M15 16h10M12 27h16M12 32h16"/></svg></div>
    <h3>Personal Injury Medical Records<br>Summaries and Reports</h3>
    <p>Partnering with several law firms, we have developed expertise in various litigation support do</p>
  </article>
  <div class="btn" style="left:312px;top:1874px;width:146px;height:40px">View More <span class="dot"></span></div>
  <article class="svc-card" style="left:618px">
    <div class="svc-photo" role="img" aria-label="Photo of hands pointing at a laptop and a printed medical report" style="background:linear-gradient(135deg,#e2e6ea 0%,#bfc8d1 40%,#8d9bab 70%,#d7dde3 100%)"></div>
    <div class="svc-icon"><svg width="40" height="44" viewBox="0 0 40 44" fill="none" stroke="#fff" stroke-width="2"><rect x="6" y="6" width="24" height="32" rx="3"/><path d="M13 6V3h10v3M12 18a5 5 0 0010 0v-4M30 24a6 6 0 11-6 6"/></svg></div>
    <h3>Retrieval, Assembly &amp; Organization<br>of Medical Records</h3>
    <p>Velmarix's team includes seasoned professionals with in-depth clinical knowledge</p>
  </article>
  <div class="btn" style="left:745px;top:1874px;width:146px;height:40px">View More <span class="dot"></span></div>
</section>

<!-- FREE FIRST FILE OFFER -->
<section class="abs offer">
  <svg class="abs" style="left:0;top:0" width="912" height="350" viewBox="0 0 912 350" fill="none" stroke="rgba(255,255,255,.07)">
    <path d="M0 260 C200 120 420 320 912 90"/><path d="M0 280 C220 140 430 330 912 110"/><path d="M0 300 C240 160 440 340 912 130"/><path d="M0 240 C180 100 410 310 912 70"/>
  </svg>
  <h2>FREE FIRST FILE OFFER</h2>
  <p>Lorem ipsum dolor sit amet, consectetur adipiscing elit, sed do eiusmod tempor incididunt ut labore et dolore magna aliqua. Ut enim ad minim veniam, quis nostrud</p>
  <div class="btn">Claim Your Free File <span class="dot"></span></div>
</section>

<!-- WHY -->
<section>
  <h2 class="abs why-title">WHY VELMARIX <span class="bars"><i></i><i></i><i></i></span></h2>
  <div class="abs why-line"></div>
  <div class="why-item" style="top:2662px">
    <div class="ico"><svg width="40" height="40" viewBox="0 0 40 40" fill="none" stroke="#fff" stroke-width="2"><circle cx="24" cy="15" r="10"/><path d="M20 19l8-8M20 12h.1M28 18h.1M3 28h8l6 3h10"/></svg></div>
    <h3>Competitive Pricing</h3>
    <p>We believe that pricing is what works for both parties. We will work with you to provide competitive pricing that fits your requirements</p>
  </div>
  <div class="why-item" style="top:2802px">
    <div class="ico"><svg width="40" height="40" viewBox="0 0 40 40" fill="none" stroke="#fff" stroke-width="2"><circle cx="20" cy="11" r="5"/><circle cx="9" cy="15" r="4"/><circle cx="31" cy="15" r="4"/><path d="M11 32c0-6 4-10 9-10s9 4 9 10M2 30c0-5 3-8 7-8M38 30c0-5-3-8-7-8"/></svg></div>
    <h3>Client Format</h3>
    <p>One of our core competencies lies in the ability to deliver customized demand letters as per the client's template.</p>
  </div>
  <div class="why-item" style="top:2942px">
    <div class="ico"><svg width="40" height="40" viewBox="0 0 40 40" fill="none" stroke="#fff" stroke-width="2"><path d="M4 18l8-8 8 4 8-4 8 8-10 10-6-4-6 4z"/><path d="M14 22l4 4M18 20l4 4"/></svg></div>
    <h3>Faster Turnaround Time</h3>
    <p>Need it quick? Not to worry! Our staff is very good at working with you to accommodate your turnaround time requirements.</p>
  </div>
  <div class="btn" style="left:245px;top:3059px;width:146px;height:40px">View More <span class="dot"></span></div>
  <div class="abs why-photo" role="img" aria-label="Photo of a smiling man in a brown jacket holding a laptop"></div>
</section>

<!-- CASES -->
<section>
  <svg class="abs cases-bg" width="1200" height="640" viewBox="0 0 1200 640">
    <path d="M0 110 Q300 110 520 70 Q760 25 1200 0 L1200 640 L0 640 Z" fill="#eef3fa"/>
  </svg>
  <h2 class="section-title" style="top:3262px"><span class="bars"><i></i><i></i><i></i></span>CASES WE SUPPORT<span class="bars"><i></i><i></i><i></i></span></h2>

  <div class="hex" style="left:176px">
    <svg class="shape" width="252" height="262" viewBox="0 0 252 262"><path d="M84 14 H168 Q184 14 194 28 L238 106 Q246 122 238 138 L194 220 Q184 236 168 236 H84 Q68 236 58 220 L14 138 Q6 122 14 106 L58 28 Q68 14 84 14Z" fill="#fff" stroke="#d7dfe9" stroke-width="2"/></svg>
    <div class="tab"><svg width="26" height="30" viewBox="0 0 26 30" fill="none" stroke="#fff" stroke-width="2"><circle cx="13" cy="8" r="5"/><path d="M3 28c0-7 4-12 10-12s10 5 10 12z"/></svg></div>
    <h3>Personal Injury</h3>
    <p>With high volumes of medical records to be reviewed, lawyers handling personal</p>
    <div class="go"><svg width="10" height="16" viewBox="0 0 10 16"><path d="M2 2l6 6-6 6" fill="none" stroke="#111" stroke-width="2"/></svg></div>
  </div>

  <div class="hex active" style="left:474px">
    <svg class="shape" width="252" height="262" viewBox="0 0 252 262"><path d="M84 14 H168 Q184 14 194 28 L238 106 Q246 122 238 138 L194 220 Q184 236 168 236 H84 Q68 236 58 220 L14 138 Q6 122 14 106 L58 28 Q68 14 84 14Z" fill="#0b2a55" stroke="#d7dfe9" stroke-width="2"/></svg>
    <div class="tab"><svg width="30" height="28" viewBox="0 0 30 28" fill="none" stroke="#fff" stroke-width="2"><rect x="3" y="3" width="24" height="10" rx="2"/><path d="M3 18h24l-2 6H5z"/><circle cx="9" cy="24" r="2"/><circle cx="21" cy="24" r="2"/></svg></div>
    <h3>Mass Tort</h3>
    <p>Mass Tort is a type of civil action involving a large number of plaintiffs against</p>
    <div class="go"><svg width="10" height="16" viewBox="0 0 10 16"><path d="M2 2l6 6-6 6" fill="none" stroke="#111" stroke-width="2"/></svg></div>
  </div>

  <div class="hex" style="left:771px">
    <svg class="shape" width="252" height="262" viewBox="0 0 252 262"><path d="M84 14 H168 Q184 14 194 28 L238 106 Q246 122 238 138 L194 220 Q184 236 168 236 H84 Q68 236 58 220 L14 138 Q6 122 14 106 L58 28 Q68 14 84 14Z" fill="#fff" stroke="#d7dfe9" stroke-width="2"/></svg>
    <div class="tab"><svg width="30" height="30" viewBox="0 0 30 30" fill="none" stroke="#fff" stroke-width="2"><circle cx="15" cy="15" r="12"/><path d="M15 9v12M9 15h12"/></svg></div>
    <h3>Medical Malpractice</h3>
    <p>Medical Malpractice cases require specialty-specific expertise.</p>
    <div class="go"><svg width="10" height="16" viewBox="0 0 10 16"><path d="M2 2l6 6-6 6" fill="none" stroke="#111" stroke-width="2"/></svg></div>
  </div>
</section>

<!-- LEAVE A MESSAGE -->
<section>
  <h2 class="section-title" style="top:3806px;gap:40px"><span class="bars"><i></i><i></i><i></i></span>LEAVE A MESSAGE<span class="bars"><i></i><i></i><i></i></span></h2>
  <p class="abs msg-sub">Wish to learn more about how we can benefit your law firm, or have any questions?</p>
  <div class="field" style="left:280px;top:3932px;width:312px">Name</div>
  <div class="field" style="left:607px;top:3932px;width:314px">Email</div>
  <div class="field" style="left:280px;top:4004px;width:312px">Phone</div>
  <div class="field" style="left:607px;top:4004px;width:314px">Organization</div>
  <div class="field" style="left:280px;top:4076px;width:641px">Message</div>
  <div class="btn" style="left:527px;top:4152px;width:146px;height:40px">Submit <span class="dot"></span></div>
</section>

<!-- FOOTER -->
<footer>
  <svg class="abs footer" width="1200" height="444" viewBox="0 0 1200 444">
    <path d="M0 70 Q260 110 560 60 Q800 20 970 0 Q1080 40 1200 70 L1200 444 L0 444 Z" fill="#0b2a55"/>
    <path d="M0 86 Q300 120 600 72 Q820 38 970 22 Q1090 56 1200 86 L1200 444 L0 444 Z" fill="#050608"/>
  </svg>
  <div class="abs logo" style="left:155px;top:4458px"><span class="mark"></span>Velmarix</div>
  <div class="abs social"><span></span><span></span><span></span></div>

  <div class="foot-col" style="left:368px">
    <h4>Business Inquiries</h4>
    <div class="foot-row"><svg width="9" height="12" viewBox="0 0 9 12"><path d="M4.5 0A4.5 4.5 0 000 4.5C0 8 4.5 12 4.5 12S9 8 9 4.5A4.5 4.5 0 004.5 0z" fill="#fff"/><circle cx="4.5" cy="4.5" r="1.6" fill="#050608"/></svg><span>4120 Harbor Crest Ave, Suite 3B<br>Coral Point, FL 33920</span></div>
    <div class="foot-row" style="margin-top:10px"><svg width="12" height="12" viewBox="0 0 24 24"><path d="M6.6 10.8a15 15 0 006.6 6.6l2.2-2.2a1 1 0 011-.25 11.4 11.4 0 003.6.6 1 1 0 011 1V20a1 1 0 01-1 1A17 17 0 013 4a1 1 0 011-1h3.5a1 1 0 011 1 11.4 11.4 0 00.6 3.6 1 1 0 01-.25 1z" fill="#fff"/></svg><span>(555) 214-0870</span></div>
    <div class="foot-row"><svg width="13" height="10" viewBox="0 0 13 10"><rect width="13" height="10" rx="1" fill="#fff"/><path d="M1 1l5.5 4.5L12 1" fill="none" stroke="#050608"/></svg><span>info@velmarix.com</span></div>
  </div>

  <div class="foot-col" style="left:648px">
    <h4>Records Processing</h4>
    <div class="foot-row"><svg width="9" height="12" viewBox="0 0 9 12"><path d="M4.5 0A4.5 4.5 0 000 4.5C0 8 4.5 12 4.5 12S9 8 9 4.5A4.5 4.5 0 004.5 0z" fill="#fff"/><circle cx="4.5" cy="4.5" r="1.6" fill="#050608"/></svg><span>18 Maple Ridge Road<br>Elmbrook, New York 11620</span></div>
    <div class="foot-row" style="margin-top:10px"><svg width="12" height="12" viewBox="0 0 24 24"><path d="M6.6 10.8a15 15 0 006.6 6.6l2.2-2.2a1 1 0 011-.25 11.4 11.4 0 003.6.6 1 1 0 011 1V20a1 1 0 01-1 1A17 17 0 013 4a1 1 0 011-1h3.5a1 1 0 011 1 11.4 11.4 0 00.6 3.6 1 1 0 01-.25 1z" fill="#fff"/></svg><span>(555) 214-0870</span></div>
    <div class="foot-row"><svg width="13" height="10" viewBox="0 0 13 10"><rect width="13" height="10" rx="1" fill="#fff"/><path d="M1 1l5.5 4.5L12 1" fill="none" stroke="#050608"/></svg><span>medretrieval@velmarix.com</span></div>
  </div>

  <div class="foot-col quick" style="left:931px">
    <h4>Quick Links</h4>
    <a>Home</a><a>About Us</a><a>Place your Order</a><a>Free First File Offer</a><a>Services</a><a>Transparent Pricing</a><a>Contact Us</a>
  </div>

  <div class="abs foot-rule"></div>
  <p class="abs copyright">Copyright@2024 - All Rights Reserved.Terms &amp; Conditions and Privacy Policy</p>
</footer>

</body>
</html>
```